yourSmileCare Brookvale Business Card

Please design a two sided business card that is Elegant and Professional
Add subtle elegant patterns to suit Spot UV printing/ or raised printing

Name: Dr Marcus T. Fenwick
Qualification: BDSc (QLD)
Title: Dental Surgeon, Clinical Director
Company: yourSmileCare Brookvale
Phone: (02) 7593 2268
Address: Shop 7/18-20 Lindon Ave Brookvale 2097
email: info@yoursmilecarebrookvale.com.au
Facebook: friendloop.net/yoursmilecarebrookvale

Motto:
Quality dentistry you can trust

Description of services (not compulsory):
Preventative Dentistry | General Dentistry
Cosmetic Dentistry | Teeth Whitening
Crown and Bridge | Root Canal Therapy
Veneers | Clearvono | Orthodontics
Emergency Dental Care | After Hours

Personalised Treatment Plans
Transparent Fees

Please make sure card is elegant and professional

Target Market(s)

general population, patients,
Dental sales companies, other professions

Industry/Entity Type

Dental Clinic

Contact Information for Business Card

Name: Dr Marcus T. Fenwick
Qualification: BDSc (QLD)
Phone: (02) 7593 2268
Address: Shop 7/18-20 Lindon Ave Brookvale

Motto:

Description of services (not compulsory)

Transparent Fees

Image of dental surgery optional

Please make sure card is elegant and profession

Requirements
Must have
• Logo
• Name, Title (next to name), Business
• Phone, address, facbeook
• Must have stylish design to suit SPOT UV reflective printing
Nice to have
• Subtle elegant patterns which will have Spot UV on them when printed
• Colours to match logo colour
• Description of services
Should not have
• Small fonts that are hard to read
• DO NOT PUT IMAGES OF DENTAL INSTRUMENTS OR TEETH PLEASE

```html
<!DOCTYPE html>
<html lang="en">
<head>
<meta charset="utf-8">
<title>yourSmileCare Brookvale Business Card</title>
<link rel="stylesheet" href="https://fonts.googleapis.com/css2?family=Open+Sans:wght@400;600&display=swap">
<style>
  :root {
    --backdrop: #2a2827;
    --card-dark: #0b0b0b;
    --card-light: #ffffff;
    --brand-green: #7dc243;
    --brand-grey: #8a8a8a;
    --text-grey: #5a5a5a;
    --service-grey: #a9a9a9;
  }
  * { margin: 0; padding: 0; box-sizing: border-box; }
  html, body {
    width: 1200px; height: 1200px; overflow: hidden;
    background: var(--backdrop);
    font-family: "Open Sans", Arial, sans-serif;
  }
  .canvas {
    position: relative; width: 1200px; height: 1200px;
    display: flex; flex-direction: column; align-items: center;
    justify-content: center; gap: 50px;
  }
  .card {
    position: relative; width: 945px; height: 540px;
    border-radius: 28px; overflow: hidden;
  }

  /* Front */
  .card-front { background: var(--card-dark); }
  .front-brand {
    position: absolute; top: 120px; left: 0; right: 0;
    text-align: center;
  }
  .brand-name {
    font-weight: 600; font-size: 56px; letter-spacing: -0.5px;
    color: var(--brand-green); line-height: 1.1;
  }
  .front-motto {
    margin-top: 16px; font-size: 18px; letter-spacing: 4px;
    text-transform: uppercase; color: var(--brand-grey);
  }
  .front-services {
    position: absolute; top: 300px; left: 0; right: 0;
    text-align: center; color: var(--service-grey);
    font-size: 21px; line-height: 1.6;
  }
  .front-promise {
    position: absolute; top: 420px; left: 0; right: 0;
    text-align: center; color: var(--brand-green);
    font-size: 21px; line-height: 1.5;
  }

  /* Back */
  .card-back { background: var(--card-light); }
  .identity {
    position: absolute; top: 80px; left: 0;
    display: flex; align-items: stretch;
  }
  .identity-bar { width: 26px; background: var(--brand-green); }
  .identity-text { padding-left: 30px; padding-top: 6px; }
  .person-name {
    font-weight: 600; font-size: 32px; color: var(--brand-green);
    line-height: 1.2;
  }
  .person-detail { font-size: 20px; color: var(--text-grey); line-height: 1.4; }

  .back-brand {
    position: absolute; top: 250px; right: 70px;
    display: flex; align-items: center; gap: 14px;
  }
  .brand-dot {
    width: 30px; height: 30px; border-radius: 50%;
    background: var(--brand-green); flex: none;
  }
  .back-brand .brand-name { font-size: 40px; }

  .contact-list {
    position: absolute; left: 62px; bottom: 58px;
    list-style: none; font-size: 20px; color: var(--text-grey);
  }
  .contact-list li {
    display: flex; align-items: center; gap: 14px; line-height: 1.75;
  }
  .contact-icon { width: 20px; height: 20px; flex: none; }

  .address {
    position: absolute; right: 70px; bottom: 58px;
    font-size: 20px; font-style: normal;
    color: var(--text-grey); line-height: 1.5;
  }
  .address-title { font-weight: 600; color: var(--brand-green); }
</style>
</head>
<body>
<main class="canvas">

  <section class="card card-front" aria-label="Business card front">
    <div class="front-brand">
      <div class="brand-name">yourSmileCare Brookvale</div>
      <div class="front-motto">Quality dentistry you can trust</div>
    </div>
    <p class="front-services">
      Preventative Dentistry | General Dentistry | Cosmetic Dentistry<br>
      Teeth Whitening | Crown and Bridge | Root Canal Therapy | Veneers<br>
      Clearvono | Orthodontics | Emergency Dental Care | After Hours
    </p>
    <p class="front-promise">
      Personalised Treatment Plans<br>
      Transparent Fees
    </p>
  </section>

  <section class="card card-back" aria-label="Business card back">
    <div class="identity">
      <div class="identity-bar"></div>
      <div class="identity-text">
        <div class="person-name">Dr Marcus T. Fenwick</div>
        <div class="person-detail">BDSc (QLD)</div>
        <div class="person-detail">Dental Surgeon, Clinical Director</div>
      </div>
    </div>

    <div class="back-brand">
      <span class="brand-dot"></span>
      <span class="brand-name">yourSmileCare Brookvale</span>
    </div>

    <ul class="contact-list">
      <li>
        <svg class="contact-icon" viewBox="0 0 20 20" aria-hidden="true">
          <rect width="20" height="20" rx="3" fill="#7dc243"/>
          <path d="M6 4.5l2 .3.8 3-1.3 1c.7 1.5 1.8 2.6 3.3 3.3l1-1.3 3 .8.3 2c-.2.8-.9 1.3-1.7 1.2C8.6 14.4 5.6 11.4 4.8 6.2c-.1-.8.4-1.5 1.2-1.7z" fill="#fff"/>
        </svg>
        (02) 7593 2268
      </li>
      <li>
        <svg class="contact-icon" viewBox="0 0 20 20" aria-hidden="true">
          <rect width="20" height="20" rx="3" fill="#7dc243"/>
          <rect x="4" y="6" width="12" height="8.5" rx="1" fill="#fff"/>
          <path d="M4.5 6.5L10 11l5.5-4.5" stroke="#7dc243" stroke-width="1.3" fill="none"/>
        </svg>
        info@yoursmilecarebrookvale.com.au
      </li>
      <li>
        <svg class="contact-icon" viewBox="0 0 20 20" aria-hidden="true">
          <rect width="20" height="20" rx="3" fill="#7dc243"/>
        </svg>
        friendloop.net/yoursmilecarebrookvale
      </li>
    </ul>

    <address class="address">
      <div class="address-title">yourSmileCare Brookvale</div>
      <div>Shop 7/18-20 Lindon Ave</div>
      <div>Brookvale 2097</div>
    </address>
  </section>

</main>
</body>
</html>
```